New Packaging and label for New Beard Oil and Shampoo brand from London

Oils, Shampoo ect .. Beard Oil Ingredients: Application Directions: Apply to beard by weight in a small amount of oil will naturally absorb. Leaving it soft & conditioned. Ingredients: Coconut oil, scented oil, Oud oil, vitamin E 100% Natural `i will have 5 types of oils Vanilla Oud Rose Oud Cocktail Tea tree Velvet Dusk

Target Market(s)

A fashionable well groomed professional gentleman who is willing to invest in his appearance.

Industry/Entity Type

It Company

Font styles to use
Sans Serif

Colors

Designer to choose colors to be used in the design.

Requirements
Must have
• Beard Oil Ingredients: Application Directions: Apply to a beard by a small amount of oil will naturally absorb. Leaving it soft & conditioned. Ingredients: Coconut Oil, Scented Oil, Oil Oud, Vitamin E 100% Natural 1.0z 30ml Made in Uk i will have 5 types of oils Vanilla Oud Rose Oud Cocktail Tea Tree Velvet Beard Dusk Shampoo APPLICATION DIRECTIONS Massage into the beard / hair and rinse out with warm water. Distorted shampoos, there are no nasty chemicals which are damaging your beard instead of the wheat proteins and oils that you add to the hair follicles with nutrients and naturally adding a protective coating. INGREDIENTS Aqua (Water), Capryl / caprylyl glucoside, Cocomidopropyl betaine, Glycerin (Veg), Xanthan gum, Phenoxyethanol, Hydrolysed wheat protein, Aloe barbadensis (Aloe vera) leaf powder, Sodium benzoate, Potassium sorbate1 3.4 oz, 100ml Cylinder packaging for the Oils, Box for the shampoo
Nice to have
• I want "London" written underneath the logo and oil name.

```html
<!DOCTYPE html>
<html lang="en">
<head>
<meta charset="utf-8">
<title>Ashcombe Beard – Vanilla Oud Beard Oil Label</title>
<link rel="stylesheet" href="https://fonts.googleapis.com/css2?family=Oswald:wght@300;500&family=Montserrat:wght@500;600&family=Cinzel:wght@700&display=swap">
<style>
  :root {
    --backdrop: #e4e4e4;
    --label-black: #1d1d1d;
    --ink-white: #ffffff;
    --ink-soft: #e8e8e8;
    --ink-muted: #bdbdbd;
    --gold: #d9b341;
  }
  * { box-sizing: border-box; margin: 0; padding: 0; }
  html, body {
    width: 1200px;
    height: 900px;
    overflow: hidden;
    background: var(--backdrop);
  }
  .label {
    position: absolute;
    left: 60px;
    top: 214px;
    width: 1080px;
    height: 472px;
    background: var(--label-black);
    color: var(--ink-white);
  }
  .info-panel {
    position: absolute;
    font-family: "Oswald", sans-serif;
    font-weight: 300;
    font-size: 21px;
    line-height: 27px;
    color: var(--ink-soft);
  }
  .info-panel h2 {
    font-family: "Oswald", sans-serif;
    font-weight: 500;
    font-size: 21px;
    line-height: 27px;
    color: var(--ink-white);
    text-transform: uppercase;
  }
  .ingredients { left: 44px; top: 112px; width: 160px; }
  .natural-claim {
    margin-top: 12px;
    font-weight: 500;
    color: var(--ink-white);
  }
  .origin {
    margin-top: 12px;
    color: var(--ink-muted);
  }
  .directions { left: 908px; top: 160px; width: 150px; }
  .front-panel {
    position: absolute;
    left: 300px;
    width: 480px;
    top: 0;
    height: 100%;
    text-align: center;
  }
  .brand-name {
    position: absolute;
    left: 0; right: 0;
    top: 120px;
    font-family: "Montserrat", sans-serif;
    font-weight: 600;
    font-size: 50px;
    line-height: 1;
    letter-spacing: 1px;
    color: var(--ink-white);
  }
  .city {
    position: absolute;
    left: 0; right: 0;
    top: 250px;
    font-family: "Montserrat", sans-serif;
    font-weight: 500;
    font-size: 32px;
    letter-spacing: 9px;
    color: var(--ink-white);
  }
  .scent {
    position: absolute;
    left: 0; right: 0;
    top: 330px;
    font-family: "Cinzel", serif;
    font-weight: 700;
    font-size: 34px;
    letter-spacing: 5px;
    color: var(--gold);
  }
  .volume {
    position: absolute;
    left: 0; right: 0;
    top: 414px;
    font-family: "Montserrat", sans-serif;
    font-weight: 500;
    font-size: 20px;
    color: var(--ink-white);
  }
</style>
</head>
<body>
  <section class="label" aria-label="Beard oil label">
    <div class="info-panel ingredients">
      <h2>Ingredients:</h2>
      <p>Coconut oil, scented oil, Oud oil, vitamin E</p>
      <p class="natural-claim">100% Natural</p>
      <p class="origin">Made in Uk</p>
    </div>

    <div class="front-panel">
      <h1 class="brand-name">ASHCOMBE BEARD</h1>
      <p class="city">LONDON</p>
      <p class="scent">VANILLA OUD</p>
      <p class="volume">1.0z /30ml</p>
    </div>

    <div class="info-panel directions">
      <h2>Directions:</h2>
      <p>Apply to beard by rubbing in a small amount the oil will naturally absorb. Leaving it soft &amp; conditioned.</p>
    </div>
  </section>
</body>
</html>
```